Visitenkarten-Design für eine Ernährungsberaterin
Zielgruppe
Ich bin Ernährungsberaterin. Meine Zielgruppe sind alle Menschen, die sich bewusster ernähren möchten.
Aufgabenstellung
Vorderseite ein Logo, welches Ernährung mit Gesundheit vereint.
Auch auf der Vorderseite ein Slogan, wie zum Beispiel, dass Gesundheit keine Frage des Alters ist... gerne etwas Kreativeres.
Das Design sollte dabei ansprechend und etwas verspielt sein.
Rückseite Adressdaten und meine Leistungen.

```html
<!DOCTYPE html>
<html lang="de">
<head>
<meta charset="utf-8">
<title>Visitenkarte Miriam Kolbeck – Ernährungsberatung</title>
<link rel="stylesheet" href="https://fonts.googleapis.com/css2?family=League+Spartan:wght@300;400&family=Yellowtail&display=swap">
<style>
  :root {
    --backdrop: #efece2;
    --leaf: #a3ca78;
    --coral: #ec7162;
    --paper: #f4f4f2;
    --ink: #6a6a6a;
    --white: #ffffff;
  }
  * { box-sizing: border-box; margin: 0; padding: 0; }
  html, body {
    width: 888px; height: 1200px; overflow: hidden;
    background: var(--backdrop);
  }
  .sheet {
    position: relative; width: 888px; height: 1200px;
    display: flex; justify-content: center; align-items: center; gap: 30px;
  }
  .card {
    position: relative; width: 401px; height: 620px;
  }
  .card--front { background: var(--leaf); }
  .card--back { background: var(--paper); }

  .brandmark {
    position: absolute; left: 0; right: 0;
    display: flex; flex-direction: column; align-items: center;
  }
  .brandmark__circle {
    border-radius: 50%; border-style: solid;
  }
  .brandmark__name {
    font-family: "League Spartan", sans-serif; font-weight: 400;
    letter-spacing: 0.08em; text-transform: uppercase;
  }
  .card--front .brandmark { top: 150px; gap: 18px; }
  .card--front .brandmark__circle {
    width: 130px; height: 130px; border-width: 3px; border-color: var(--coral);
  }
  .card--front .brandmark__name { color: var(--coral); font-size: 20px; }

  .card--back .brandmark { top: 100px; gap: 10px; }
  .card--back .brandmark__circle {
    width: 74px; height: 74px; border-width: 2px; border-color: var(--leaf);
  }
  .card--back .brandmark__name { color: var(--leaf); font-size: 13px; }

  .slogan {
    position: absolute; left: 0; right: 0; top: 418px;
    text-align: center; color: var(--white);
    font-family: "Yellowtail", cursive; font-size: 38px; line-height: 58px;
  }

  .owner {
    position: absolute; left: 0; right: 0; top: 272px;
    text-align: center; color: var(--coral);
    font-family: "Yellowtail", cursive; font-size: 52px; line-height: 1.1;
  }
  .service {
    position: absolute; left: 0; right: 0; top: 360px;
    text-align: center; color: var(--ink);
    font-family: "League Spartan", sans-serif; font-weight: 300;
    font-size: 22px; line-height: 28px; letter-spacing: 0.06em;
  }
  .contact {
    position: absolute; left: 66px; top: 458px;
    list-style: none;
    font-family: "League Spartan", sans-serif; font-weight: 300;
    font-size: 19px; letter-spacing: 0.05em; color: var(--ink);
  }
  .contact__item {
    display: flex; align-items: center; gap: 12px; height: 34px;
  }
  .contact__icon { width: 22px; height: 22px; flex: none; }
</style>
</head>
<body>
<main class="sheet">
  <section class="card card--front" aria-label="Vorderseite">
    <div class="brandmark">
      <div class="brandmark__circle"></div>
      <span class="brandmark__name">Miriam Kolbeck</span>
    </div>
    <p class="slogan">gesund geht durch<br>den Mund</p>
  </section>

  <section class="card card--back" aria-label="Rückseite">
    <div class="brandmark">
      <div class="brandmark__circle"></div>
      <span class="brandmark__name">Miriam Kolbeck</span>
    </div>
    <h1 class="owner">Miriam Kolbeck</h1>
    <p class="service">Ernährungsberatung<br>für jedes Alter</p>
    <ul class="contact">
      <li class="contact__item">
        <svg class="contact__icon" viewBox="0 0 24 24" fill="none" stroke="#a3ca78" stroke-width="1.6" stroke-linejoin="round" aria-hidden="true">
          <path d="M5 3h4l2 5-2.5 1.5a11 11 0 0 0 6 6L16 13l5 2v4a2 2 0 0 1-2 2A16 16 0 0 1 3 5a2 2 0 0 1 2-2z"/>
        </svg>
        <span>+34 9876 543210</span>
      </li>
      <li class="contact__item">
        <svg class="contact__icon" viewBox="0 0 24 24" fill="none" stroke="#a3ca78" stroke-width="1.6" aria-hidden="true">
          <rect x="2" y="5" width="20" height="14"/>
          <path d="M2 5l10 8 10-8M2 19l7-7M22 19l-7-7"/>
        </svg>
        <span>info@miriam-kolbeck.de</span>
      </li>
      <li class="contact__item">
        <svg class="contact__icon" viewBox="0 0 24 24" fill="none" stroke="#a3ca78" stroke-width="1.6" aria-hidden="true">
          <circle cx="12" cy="12" r="10"/>
          <ellipse cx="12" cy="12" rx="4.5" ry="10"/>
          <path d="M2 12h20M4 7h16M4 17h16"/>
        </svg>
        <span>www.miriam-kolbeck.de</span>
      </li>
    </ul>
  </section>
</main>
</body>
</html>
```